We are looking to design a black on white bourbon label for a new brand
in att we have added
1. the bottle we need to use (wine bottle in black)
2. some industry examples (Look at horse rider label good example of where we need to go)
3. horses and cowboys illistrations

The brand will be Called OLD BRASS LANTERN. we want an old school feeling label prohibition style.

What we need on the label is
1. visual = Bucking Horse + rider cowboy + lasso forming a circle
2. Name = Old Brass Lantern Bourbon Straight Aged Whiskey
3. Product info = 70 CL 40 ABV
4. Distilled in the Wild Wild West WWW.OLDBRASSLANTERNSPIRITS.COM

```html
<!DOCTYPE html>
<html lang="en">
<head>
<meta charset="utf-8">
<title>Old Brass Lantern Bourbon Label</title>
<link rel="stylesheet" href="https://fonts.googleapis.com/css2?family=Alfa+Slab+One&family=Cinzel:wght@900&family=Old+Standard+TT:wght@700&display=swap">
<style>
  :root {
    --ink: #111111;
    --paper: #ffffff;
    --backdrop: #e9e9ea;
    --art-light: #d9d9d9;
    --art-dark: #6a6a6a;
  }
  html, body {
    margin: 0;
    padding: 0;
    width: 1200px;
    height: 612px;
    overflow: hidden;
    background: var(--backdrop);
  }
  .stage {
    position: relative;
    width: 1200px;
    height: 612px;
  }
  .label {
    position: absolute;
    left: 300px;
    top: 30px;
    width: 600px;
    height: 552px;
    display: block;
  }
  .label text {
    text-rendering: geometricPrecision;
    -webkit-font-smoothing: antialiased;
  }
  .title-word { font-family: "Alfa Slab One", serif; fill: var(--ink); }
  .western { font-family: "Cinzel", serif; font-weight: 900; fill: var(--ink); }
  .western-reverse { font-family: "Cinzel", serif; font-weight: 900; fill: var(--paper); }
  .badge-text { font-family: "Old Standard TT", serif; font-weight: 700; fill: var(--paper); }
  .rule { stroke: var(--ink); fill: none; }
</style>
</head>
<body>
<main class="stage">
  <svg class="label" viewBox="0 0 600 552" xmlns="http://www.w3.org/2000/svg" aria-label="Old Brass Lantern bourbon label">
    <defs>
      <linearGradient id="art-tone" x1="0" y1="0" x2="0" y2="1">
        <stop offset="0" stop-color="#d9d9d9"/>
        <stop offset="1" stop-color="#6a6a6a"/>
      </linearGradient>
    </defs>

    <rect class="label-paper" x="0" y="0" width="600" height="552" fill="var(--paper)"/>
    <rect class="label-top-rule" x="0" y="0" width="600" height="4" fill="var(--ink)"/>
    <rect class="label-foot-band" x="0" y="526" width="600" height="26" fill="var(--ink)"/>

    <g class="top-rails">
      <line class="rule" x1="36" y1="46" x2="175" y2="46" stroke-width="3"/>
      <line class="rule" x1="44" y1="54" x2="175" y2="54" stroke-width="1.2"/>
      <line class="rule" x1="52" y1="61" x2="175" y2="61" stroke-width="1.2"/>
      <line class="rule" x1="175" y1="58" x2="395" y2="36" stroke-width="1.2"/>
    </g>

    <g class="upper-diagonal">
      <line class="rule" x1="228" y1="115" x2="400" y2="68" stroke-width="3"/>
      <line class="rule" x1="228" y1="124" x2="402" y2="78" stroke-width="1.2"/>
    </g>

    <g class="lower-diagonal">
      <line class="rule" x1="228" y1="410" x2="560" y2="382" stroke-width="3"/>
      <line class="rule" x1="300" y1="414" x2="560" y2="392" stroke-width="1.2"/>
    </g>

    <text class="western premium-line" x="44" y="92" font-size="20">PREMIUM QUALITY</text>

    <text class="title-word" x="410" y="70" font-size="46" textLength="148" lengthAdjust="spacingAndGlyphs">OLD</text>
    <text class="title-word" x="250" y="240" font-size="120" textLength="300" lengthAdjust="spacingAndGlyphs">BRASS</text>
    <text class="title-word" x="250" y="370" font-size="120" textLength="300" lengthAdjust="spacingAndGlyphs">LANTERN</text>

    <rect class="hero-art" x="22" y="100" width="200" height="395" rx="4" fill="url(#art-tone)"
          role="img" aria-label="Illustration: cowboy on a bucking horse swinging a lasso that forms a circle, desert cacti, birds and a fence"/>

    <g class="volume-badge">
      <circle cx="270" cy="462" r="39" fill="var(--paper)" stroke="var(--ink)" stroke-width="1.5"/>
      <circle cx="270" cy="462" r="35" fill="var(--ink)"/>
      <text class="badge-text" x="270" y="443" font-size="7" text-anchor="middle">VOLUME</text>
      <text class="badge-text" x="270" y="463" font-size="18" text-anchor="middle">70CL</text>
      <text class="badge-text" x="270" y="484" font-size="18" text-anchor="middle">40ABV</text>
    </g>

    <text class="western" x="330" y="440" font-size="30" textLength="226" lengthAdjust="spacingAndGlyphs">BOURBON</text>
    <rect class="descriptor-bar" x="320" y="449" width="243" height="25" fill="var(--ink)"/>
    <text class="western-reverse" x="330" y="468" font-size="18" textLength="224" lengthAdjust="spacingAndGlyphs">STRAIGHT AGED</text>
    <text class="western" x="330" y="508" font-size="30" textLength="226" lengthAdjust="spacingAndGlyphs">WHISKEY</text>

    <text class="western site-url" x="40" y="514" font-size="11" textLength="266" lengthAdjust="spacingAndGlyphs">WWW.OLDBRASSLANTERNSPIRITS.COM</text>
  </svg>
</main>
</body>
</html>
```